Animal Adoption Page

We are working on re-designing an animal adoption page for one of our clients, and are failing to come up with a modern, cutting edge design that not only looks great, but converts well also. We would like to reach out to the brightpanel community to see some innovative design work that will help us to reach our goal. Unfortunately we can't release details of our client, so the design will need to be based on some generalisations and assumptions.
Firstly, here are some competitor pages to give you an idea of the typical animal adoption process:
- https://help.plovernet.org.uk/
- http://www.trailhounds.org.uk/microsites/sponsor-a-puppy
- http://www.halvorne.org/adopt
- http://www.globalcreaturehaven.org/adopt-an-animal
- http://www.tolbrecktrust.org/adopt
- http://www.fenstead.org.uk/adopt/default.asp
- https://give.openplains.org.uk/adopt
- http://www.qvb.org/shop/animal-adoptions/category.html
- http://www.bramleypark.org/support-us/adoptions
Secondly, here are some details that you should assume about the client:
1. Our client is heavily involved in animal conservation and have a number of animal parks/zoos in the UK
2. They have about 30 animals available for adoption, spread across 6 or 7 species (such as big cats, gorillas, elephants, etc.)
3. Each animal that you can adopt has a name, a biography, facts and personal info (date of birth, keeper, etc.)
4. There are several adoption packages to choose from:
"junior" which is aimed at children and comes with a free cuddly toy
"standard" which is aimed at everyone and has 4 different pricing levels. Each level has slightly different benefits, but usually contain an annual pass to one of the organisations animal parks/zoos. For the purposes of the design, you can choose the names of each pricing level (or if you'd prefer call them level 1, level 2, level 3 and level 4)
"virtual" is aimed at people who do not want the physical goods that come with the other adoptions packages, and just want the good feeling of helping an animal
The typical purchaser of an adoption has the following properties:
1. Most people who purchase adoptions are aged 20-45
2. Adoptions are mostly purchased BY females
3. Most adoptions are purchased FOR women
4. The majority of adoptions are purchased as gifts for other people (about 75%)
5. Gifters (people who purchase gifts for others) are the primary market we're trying to reach with the page, but other types of adopters do exist (animal lovers, people who enjoy conservation, people who want more than just a ticket to one of the parks/zoos) and these should be catered for also
What MUST the design incorporate?
- The design must show a complete design for the adoption purchase process. This includes the first page they see when they click on the "adopt" navigation link, the animal selection process, the adoption package selection process, how animal details are displayed during the process and the checkout process.
- The process must be clear and concise and very user friendly
- The design must use high quality imagery throughout. Only real photos of animals are allowed (no drawings or cartoons) but animal silhouettes are acceptable. A selection of high quality images have been provided to help guide you but you are in no way limited to using these
What SHOULD the design incorporate
- We'd like the final deign to be based on a single page website concept. You can get lots of inspiration from here - http://www.plinthgallery.com/websites/parallax/. The closest design from the current competitors is the one for halvorne.org
- The process must take into consideration conversion rates and try to be optimised
- You can design the page to use any sort of fancy javascript or jquery effects and animation. there is no need to code these, just describe how the effects will work in a document (with images where applicable)
- The design will ideally be image led, with nice large background images
What DOES NOT need to be included
- A logo design - just use a placeholder
- Any HTML or Javascript - we just need a high quality layered photoshop file from the winner
- Copy - Feel free to use lorem ipsum text where copy should go, but please describe what the copy is intended to be about either in the design or in a separate document (e.g. box 1 should contain a description of the animal species)
Colours/Brand
The new website that is being designed for the client uses two fonts throughout. For headings they use Helvetica Neue 97 Black Condensed, and for body text they use Futura PT. If you do not have these fonts, you can use equivalents but try to keep them as close to the originals as possible.
Throughout the site pages, the fonts tend to be white, and are against dark earthy coloured backgrounds. The primary palette of the site is earthy colours such as browns, greens, oranges and greys. Black is also featured heavily as a background colour.
The site comprises of lots of large background images which take up most of the users browser viewport. By default we'd like you to continue this on the adoption pages, but we're open to suggestions.
When large background images are used, and text needs to be placed over the top, the site uses semi-opaque rectangles (either 28%, 64% or 84%) as a background to the text.
Overall the site uses largely flat design principles, and when there are buttons for the user to click on, they are placed on flat rectangles (not rounded) with solid background colours.
Last comments
Overall, we are looking for something unique and cutting edge. Over the years, our client has tried using most of the approaches currently followed by our competitors with varying levels of success, but ultimately we feel there is a lot that can be done to improve the process, and are looking for a forward thinking design, that use as many cutting edge technology and design concepts as needed. We are not afraid to push the boundaries of technology and design - so feel free to think a little radically.
The winning design will be the one that provides us with the most inspiration for our final design. There are secondary prizes for any other designs that provide us with significant inspiration for our final design.
UPDATE 1: A number of designers have asked us whether the designs need to include a mobile interface. We can confirm that the smallest screensize we expect to view this page is a portrait tablet, with a screen resolution of 720px x 1024px. Anything smaller than this will be served by a separate mobile site that we will design.
UPDATE 2: From the designs we have received so far they have all had a key element missing, and we have realised this wasn't explained well enough in the original brief. We would like to see a thank you page or panel that will be displayed to the user after they have made an adoption. The elements that should be visible on this page are: 1) a thank you message, 2) the ability to share the adoption on their social networks, 3) an encouragement to share their adoption certificate on their chatterly account (probably by installing a custom chatterly app) and 4) to download a mobile app that they get free as part of their adoption
Reason: Due to requests from a few different designers we have decided to extend the deadline of this project by 5 days. This will enable all designers who have taken part to revise their designs in accordance with our feedback and provide an opportunity for new designers to submit design ideas.
- Helvetica Neue 97 black Condensed (for headers), Futura PT Body (for body)

```html
<!DOCTYPE html>
<html lang="en">
<head>
<meta charset="utf-8">
<title>Junior Adoption Package – Levels</title>
<link href="https://fonts.googleapis.com/css2?family=Arimo:wght@400;700&family=Inter:wght@100;300&display=swap" rel="stylesheet">
<style>
  :root {
    --ink: #ffffff;
    --night: #120c06;
    --mane-dark: #3a220c;
    --mane: #8a5419;
    --mane-light: #c98a3a;
    --gold: #e9b868;
    --gold-deep: #a86e22;
    --sand: #a69f85;
    --sand-light: #c2bca4;
    --sand-dark: #8f8769;
    --rule: rgba(255,255,255,0.9);
    --digit: rgba(255,255,255,0.55);
    --button-face: rgba(255,255,255,0.9);
    --button-ink: #6a4316;
  }
  * { box-sizing: border-box; margin: 0; padding: 0; }
  html, body { width: 1200px; height: 744px; overflow: hidden; background: var(--night); }
  body { font-family: "Arimo", Helvetica, Arial, sans-serif; color: var(--ink); }

  .page { position: relative; width: 1200px; height: 744px; display: flex; }

  /* Package panel */
  .package {
    position: relative; width: 598px; height: 744px; text-align: center;
  }
  .package__photo {
    position: absolute; inset: 0;
    background:
      radial-gradient(ellipse 60% 50% at 25% 30%, var(--mane-light) 0%, transparent 70%),
      radial-gradient(ellipse 55% 60% at 55% 75%, var(--mane) 0%, transparent 75%),
      linear-gradient(100deg, var(--mane-dark) 0%, var(--mane) 40%, var(--night) 100%);
  }
  .package__shade { position: absolute; inset: 0; background: rgba(0,0,0,0.28); }
  .package__title {
    position: absolute; top: 56px; left: 0; width: 100%;
    font-size: 44px; font-weight: 700; letter-spacing: -0.5px;
  }
  .price-badge { position: absolute; left: 185px; top: 163px; width: 220px; height: 220px; }
  .price-badge__value {
    position: absolute; left: 185px; top: 252px; width: 220px;
    font-size: 34px; font-weight: 400;
  }
  .package__audience {
    position: absolute; top: 438px; left: 0; width: 100%;
    font-size: 34px; line-height: 58px;
  }
  .package__audience strong { font-weight: 700; }

  .back-frame {
    position: absolute; left: 106px; top: 574px; width: 368px; height: 112px;
    border: 14px solid rgba(168,110,34,0.55);
    outline: 2px solid rgba(233,184,104,0.5); outline-offset: -2px;
  }
  .back-button {
    position: absolute; left: 120px; top: 590px; width: 340px; height: 80px;
    background: var(--button-face); border: none;
    display: flex; align-items: center; justify-content: center; gap: 16px;
    font-family: inherit; font-size: 29px; font-weight: 700; color: var(--button-ink);
  }

  /* Levels panel */
  .levels { position: relative; width: 602px; height: 744px; }
  .levels__photo {
    position: absolute; inset: 0;
    background:
      radial-gradient(ellipse 40% 45% at 40% 60%, var(--sand-light) 0%, transparent 70%),
      linear-gradient(180deg, var(--sand-dark) 0%, var(--sand) 50%, var(--sand-dark) 100%);
  }
  .levels__grid {
    position: absolute; inset: 0;
    display: grid; grid-template-columns: 300px 300px; grid-template-rows: 186px 186px 184px 184px;
    column-gap: 2px; row-gap: 2px; background: var(--rule);
  }
  .level-name, .level-text { background: rgba(166,159,133,0.55); position: relative; }
  .levels__grid > * { background-color: transparent; }
  .levels__grid { background: none; }
  .rule-v { position: absolute; left: 300px; top: 0; width: 2px; height: 744px; background: var(--rule); }
  .rule-h { position: absolute; left: 0; width: 602px; height: 2px; background: var(--rule); }

  .level-name__digit {
    position: absolute; left: 36px; top: 22px;
    font-family: "Inter", "Helvetica Neue", sans-serif; font-weight: 100;
    font-size: 124px; line-height: 1; color: var(--digit);
  }
  .level-name__label {
    position: absolute; left: 148px; top: 76px;
    font-family: "Inter", "Helvetica Neue", sans-serif; font-weight: 300;
    font-size: 31px; letter-spacing: -0.5px; color: var(--ink);
  }
  .level-text p {
    position: absolute; left: 28px; top: 48px; width: 232px;
    font-size: 11px; line-height: 18px; font-weight: 700; letter-spacing: 0.2px;
  }
</style>
</head>
<body>
<main class="page">
  <section class="package">
    <div class="package__photo" role="img" aria-label="Close-up photograph of a resting lion with a golden mane"></div>
    <div class="package__shade"></div>
    <h1 class="package__title">Junior</h1>
    <svg class="price-badge" viewBox="0 0 220 220" aria-hidden="true">
      <defs>
        <linearGradient id="ring" x1="0" y1="0" x2="1" y2="1">
          <stop offset="0" stop-color="#a86e22"/>
          <stop offset="0.5" stop-color="#f3cf8a"/>
          <stop offset="1" stop-color="#e9b868"/>
        </linearGradient>
      </defs>
      <circle cx="110" cy="110" r="106" fill="rgba(18,12,6,0.64)" stroke="url(#ring)" stroke-width="5"/>
    </svg>
    <div class="price-badge__value">$69</div>
    <p class="package__audience">For <strong>Everyone</strong><br>an annual pass</p>
    <div class="back-frame"></div>
    <button class="back-button" type="button">
      <svg width="44" height="34" viewBox="0 0 44 34" aria-hidden="true">
        <path d="M18 2 L2 15 L18 28 L18 20 C28 19 36 23 42 32 C40 18 32 10 18 9 Z" fill="#4a2e10"/>
      </svg>
      Back
    </button>
  </section>

  <section class="levels">
    <div class="levels__photo" role="img" aria-label="Photograph of pale fallow deer with antlers in a misty field"></div>
    <div class="rule-v"></div>
    <div class="rule-h" style="top:186px"></div>
    <div class="rule-h" style="top:373px"></div>
    <div class="rule-h" style="top:558px"></div>
    <div class="levels__grid">
      <div class="level-name"><span class="level-name__digit">1</span><span class="level-name__label">Level1</span></div>
      <div class="level-text"><p>Desciption of level1: Lorem ipsum dolor sit amet, consectetur adipiscing elit. Duis tincidunt odio eu magna dictum ut bibendum nulla faucibus. Aenean eget dui nulla. Sed congue adipiscing elit.</p></div>
      <div class="level-name"><span class="level-name__digit">2</span><span class="level-name__label">Level2</span></div>
      <div class="level-text"><p>Desciption of level1: Lorem ipsum dolor sit amet, consectetur adipiscing elit. Duis tincidunt odio eu magna dictum ut bibendum nulla faucibus. Aenean eget dui nulla. Sed congue adipiscing elit.</p></div>
      <div class="level-name"><span class="level-name__digit">3</span><span class="level-name__label">Level3</span></div>
      <div class="level-text"><p>Desciption of level1: Lorem ipsum dolor sit amet, consectetur adipiscing elit. Duis tincidunt odio eu magna dictum ut bibendum nulla faucibus. Aenean eget dui nulla. Sed congue adipiscing elit.</p></div>
      <div class="level-name"><span class="level-name__digit">4</span><span class="level-name__label">Level4</span></div>
      <div class="level-text"><p>Desciption of level1: Lorem ipsum dolor sit amet, consectetur adipiscing elit. Duis tincidunt odio eu magna dictum ut bibendum nulla faucibus. Aenean eget dui nulla. Sed congue adipiscing elit.</p></div>
    </div>
  </section>
</main>
</body>
</html>
```